Business Card for Academic Coach

I need a business card designed for me - a private tutor/academic coach.

Glen Marlowe
Academic Coach
AB Velden University, 1994 Cum Laude
Phone: 555-317-8842
glenmmarlowe@quillpost.example

Subjects
LRT and MQE
Math, Physics, Writing

Industry/Entity Type

Business

```html
<!DOCTYPE html>
<html lang="en">
<head>
<meta charset="utf-8">
<title>Glen Marlowe – Academic Coach Business Card</title>
<link rel="stylesheet" href="https://fonts.googleapis.com/css2?family=Tenor+Sans&family=Arimo:wght@400&display=swap">
<style>
  :root {
    --page: #ffffff;
    --card-dark: #333333;
    --card-light: #ffffff;
    --ink: #1e1e1e;
    --ink-light: #ffffff;
    --name-accent: #2b1f5e;
    --frame: #111111;
  }
  * { margin: 0; padding: 0; box-sizing: border-box; }
  html, body {
    width: 1200px; height: 979px; overflow: hidden;
    background: var(--page);
  }
  .canvas { position: relative; width: 1200px; height: 979px; }

  .card { position: absolute; width: 396px; height: 693px; }
  .card--back { left: 151px; top: 116px; background: var(--card-dark); }
  .card--front { left: 609px; top: 116px; background: var(--card-light); border: 2px solid var(--frame); }

  .caps {
    position: absolute; left: 0; width: 100%; text-align: center;
    font-family: "Tenor Sans", sans-serif; font-variant: small-caps;
    letter-spacing: 1.5px; white-space: nowrap;
  }
  .back-name { top: 76px; font-size: 30px; color: var(--ink-light); }
  .back-title { top: 143px; font-size: 30px; color: var(--ink-light); }
  .back-degree { top: 206px; font-size: 22px; line-height: 27px; color: var(--ink-light); }

  .services {
    position: absolute; left: 27px; top: 342px; width: 340px; height: 311px;
    background: var(--card-light); color: var(--ink);
    font-family: "Arimo", sans-serif; text-align: center;
  }
  .services p { position: absolute; left: 0; width: 100%; white-space: nowrap; }
  .services .subjects-1 { top: 41px; font-size: 21px; }
  .services .subjects-2 { top: 86px; font-size: 21px; }
  .services .subjects-3 { top: 130px; font-size: 21px; }
  .services .phone { top: 200px; font-size: 21px; }
  .services .email { top: 242px; font-size: 18px; }

  .brand {
    position: absolute; left: 40px; top: 64px; width: 293px; height: 204px;
    display: flex; align-items: center; justify-content: center; gap: 14px;
  }
  .brand-square { width: 56px; height: 56px; background: var(--card-dark); flex: none; }
  .brand-name {
    font-family: "Tenor Sans", sans-serif; font-variant: small-caps;
    font-size: 30px; color: var(--card-dark); letter-spacing: 1px; white-space: nowrap;
  }
  .front-name { top: 363px; font-size: 40px; color: var(--name-accent); }
  .front-title { top: 421px; font-size: 32px; color: var(--ink); }
</style>
</head>
<body>
<main class="canvas">
  <section class="card card--back" aria-label="Card back">
    <p class="caps back-name">Glen Marlowe</p>
    <p class="caps back-title">Academic Coach</p>
    <p class="caps back-degree">AB Velden University<br>1994 Cum Laude</p>
    <div class="services">
      <p class="subjects-1">LRT &amp; MQE</p>
      <p class="subjects-2">Math, Physics,</p>
      <p class="subjects-3">&amp; Writing</p>
      <p class="phone">555-317-8842</p>
      <p class="email">glenmmarlowe@quillpost.example</p>
    </div>
  </section>

  <section class="card card--front" aria-label="Card front">
    <div class="brand">
      <span class="brand-square"></span>
      <span class="brand-name">Glen Marlowe</span>
    </div>
    <p class="caps front-name">Glen Marlowe</p>
    <p class="caps front-title">Academic Coach</p>
  </section>
</main>
</body>
</html>
```